Calveth Medical Business Card Design

This is a private medical device company. We recently launched the new website and would like to redesign the business cards. Please see the website: www.orlenmedical.example. We'd like to keep the cards simple and professional but modern to match the website and collateral branding. Our customers are physicians and investors. I have attached the old design for comparison. I have also attached the updated logo. Please note the business card information will change, based on all employees who need to order them. So I will need to be able easily edit the copy.
Updates

Hi designers-thank you very much for submitting designs. I look forward to the results!! Joan

Target Market(s)

Our target audience are physicians

Industry/Entity Type

Medical

Contact Information for Business Card

Dorothy Wensley
Director of Marketing and Reimbursement
dwensley@orlenmedical.example
M: xxx-xxx-xxxx
O: xxx-xxx-xxxx
4120 Pinto Ridge Rd.
Suite 610
Austin, TX 78592

Font styles to use
Sans Serif

Requirements
Must have
• Must include the logo and a color or color from the logo and branding
Nice to have
• Maybe include the logo icon on the back.

```html
<!DOCTYPE html>
<html lang="en">
<head>
<meta charset="utf-8">
<title>Calveth Medical Business Card</title>
<link rel="stylesheet" href="https://fonts.googleapis.com/css2?family=Open+Sans:wght@300;400;600&display=swap">
<style>
  :root {
    --bg: #8c8f91;
    --paper: #ffffff;
    --charcoal: #474344;
    --ink: #3b3839;
    --red: #e8324a;
    --teal: #5bb3c8;
    --light: #f2f2f2;
  }
  * { margin: 0; padding: 0; box-sizing: border-box; }
  html, body { width: 1200px; height: 771px; overflow: hidden; }
  body {
    background: var(--bg);
    font-family: "Open Sans", sans-serif;
    position: relative;
  }
  .card {
    position: absolute;
    width: 520px;
    height: 297px;
    background: var(--paper);
    overflow: hidden;
    box-shadow: 0 6px 18px rgba(0,0,0,0.25);
  }
  .card--back { left: 50px; top: 237px; }
  .card--front { left: 630px; top: 237px; }

  .brand {
    display: flex;
    align-items: center;
    gap: 12px;
    color: var(--ink);
    font-weight: 400;
    white-space: nowrap;
  }
  .brand__dot {
    border-radius: 50%;
    background: var(--teal);
    flex: none;
  }
  .card--back .brand {
    position: absolute;
    left: 50%; top: 50%;
    transform: translate(-50%, -50%);
    font-size: 44px;
    letter-spacing: -0.5px;
  }
  .card--back .brand__dot { width: 42px; height: 42px; }

  .card--front .brand {
    position: absolute;
    left: 190px; top: 50px;
    font-size: 30px;
    letter-spacing: -0.5px;
  }
  .card--front .brand__dot { width: 30px; height: 30px; }

  .band { position: absolute; inset: 0; width: 100%; height: 100%; }

  .contact {
    position: absolute;
    left: 26px; top: 118px;
    list-style: none;
    color: var(--light);
    font-size: 9.5px;
    letter-spacing: 0.6px;
    line-height: 1.45;
  }
  .contact li { display: flex; align-items: center; gap: 7px; }
  .contact__icon { width: 11px; height: 11px; flex: none; }
  .contact__spacer { width: 11px; flex: none; }

  .person {
    position: absolute;
    right: 26px; bottom: 26px;
    text-align: right;
    color: var(--light);
  }
  .person__name {
    font-size: 12px;
    font-weight: 600;
    letter-spacing: 2px;
    text-transform: uppercase;
  }
  .person__role {
    font-size: 8.5px;
    font-weight: 300;
    letter-spacing: 2.5px;
    text-transform: uppercase;
    margin-top: 2px;
  }
</style>
</head>
<body>

  <section class="card card--back" aria-label="Business card back">
    <div class="brand">
      <span class="brand__dot"></span>
      <span class="brand__name">Calveth Medical</span>
    </div>
  </section>

  <section class="card card--front" aria-label="Business card front">
    <svg class="band" viewBox="0 0 520 297" preserveAspectRatio="none" aria-hidden="true">
      <path d="M0 62 C120 70 330 150 520 222 L520 297 L0 297 Z" fill="var(--charcoal)"/>
      <path d="M0 52 C150 52 330 130 470 214 C330 140 150 66 0 60 Z" fill="var(--red)"/>
    </svg>

    <div class="brand">
      <span class="brand__dot"></span>
      <span class="brand__name">Calveth Medical</span>
    </div>

    <ul class="contact">
      <li>
        <svg class="contact__icon" viewBox="0 0 12 12" aria-hidden="true"><circle cx="6" cy="6" r="6" fill="var(--light)"/><path d="M6 2.6a2 2 0 0 0-2 2c0 1.5 2 4 2 4s2-2.5 2-4a2 2 0 0 0-2-2z" fill="var(--charcoal)"/></svg>
        <span>Suite # 610, Ridge Bldg.</span>
      </li>
      <li><span class="contact__spacer"></span><span>TX 78592</span></li>
      <li>
        <svg class="contact__icon" viewBox="0 0 12 12" aria-hidden="true"><circle cx="6" cy="6" r="6" fill="var(--light)"/><path d="M4 3h1.3l.6 1.6-.8.6a4 4 0 0 0 1.7 1.7l.6-.8 1.6.6V8a1 1 0 0 1-1 1A5 5 0 0 1 3 4a1 1 0 0 1 1-1z" fill="var(--charcoal)"/></svg>
        <span>512-555-0142</span>
      </li>
      <li>
        <svg class="contact__icon" viewBox="0 0 12 12" aria-hidden="true"><circle cx="6" cy="6" r="6" fill="var(--light)"/><rect x="4" y="2.5" width="4" height="7" rx="0.8" fill="var(--charcoal)"/></svg>
        <span>512-555-0187</span>
      </li>
      <li>
        <svg class="contact__icon" viewBox="0 0 12 12" aria-hidden="true"><circle cx="6" cy="6" r="6" fill="var(--light)"/><rect x="3" y="4.5" width="6" height="4" fill="var(--charcoal)"/><rect x="4" y="2.5" width="4" height="2" fill="var(--charcoal)"/></svg>
        <span>512-555-0163</span>
      </li>
      <li>
        <svg class="contact__icon" viewBox="0 0 12 12" aria-hidden="true"><circle cx="6" cy="6" r="6" fill="var(--light)"/><rect x="3" y="4" width="6" height="4" fill="var(--charcoal)"/><path d="M3 4l3 2.2L9 4" stroke="var(--light)" stroke-width="0.7" fill="none"/></svg>
        <span>mhale@calvethmedical.example</span>
      </li>
      <li>
        <svg class="contact__icon" viewBox="0 0 12 12" aria-hidden="true"><circle cx="6" cy="6" r="6" fill="var(--light)"/><circle cx="6" cy="6" r="3" fill="none" stroke="var(--charcoal)" stroke-width="0.8"/><path d="M3 6h6M6 3v6" stroke="var(--charcoal)" stroke-width="0.7"/></svg>
        <span>www.calvethmedical.example</span>
      </li>
    </ul>

    <div class="person">
      <p class="person__name">Marcus Hale</p>
      <p class="person__role">Owner / C.E.O</p>
    </div>
  </section>

</body>
</html>
```